Email flow for classic watch brand

We need to update our welcome flow with 3 emails. We want the design to reflect the brand and website www.kovanta.com. Our watches are unisex and the design needs to be light and modern.
The design will be the same for all but the message is different.
Email 1: Welcome
Email 2: Products
Email 3: Offer
I have attached PDFs of the emails we currently use and good examples on emails I like.
Emails need to be responsive and look great on all desktop and mobile.
Please use these lookbook images for the emails
https://files.plenmox.com/open?id=7QxRTzzn52KpfLmNDWqaVcXsTt
Kind regards
Fredrik Tolvmark
Logo and product images can be found here: https://files.plenmox.com/open?id=4H713yR8MUPLgk28jN9cWrHuKp
Target Market(s)
24-35 year olds with a fashion interest.
Industry/Entity Type
Fashion
Font styles to use
Look and feel
Each slider illustrates characteristics of the customer's brand and the style your logo design should communicate.

```html
<!DOCTYPE html>
<html lang="en">
<head>
<meta charset="utf-8">
<title>Kovanta – Welcome</title>
<link rel="stylesheet" href="https://fonts.googleapis.com/css2?family=EB+Garamond:wght@400;500;700&display=swap">
<style>
  :root {
    --ink: #1a1a1a;
    --paper: #ffffff;
    --button: #222222;
    --button-text: #ffffff;
    --coat-grey: #a9a8a6;
    --coat-dark: #6f6e6c;
    --navy: #1d2a48;
    --mist: #f1f0ee;
    --mist-deep: #dcdad6;
    --suit: #2a2b2e;
    --suit-light: #8a8985;
  }
  * { box-sizing: border-box; margin: 0; padding: 0; }
  html, body { width: 1200px; height: 2400px; overflow: hidden; background: var(--paper); }
  body { font-family: "EB Garamond", Georgia, serif; color: var(--ink); }

  .email { position: relative; width: 1200px; height: 2400px; }

  .brand {
    position: absolute; top: 290px; left: 0; width: 100%;
    text-align: center; font-size: 118px; font-weight: 500; letter-spacing: 4px; line-height: 1;
  }
  .main-nav {
    position: absolute; top: 470px; left: 0; width: 100%;
    display: flex; justify-content: center; gap: 80px;
    font-size: 56px; line-height: 1;
  }
  .headline {
    position: absolute; top: 585px; left: 0; width: 100%;
    text-align: center; font-size: 124px; font-weight: 400; letter-spacing: 30px; line-height: 1;
    padding-left: 30px;
  }

  .lookbook {
    position: absolute; top: 790px; left: 0; width: 1200px; height: 1200px;
    display: grid; grid-template-columns: 600px 600px; grid-template-rows: 600px 600px;
  }
  .tile { position: relative; overflow: hidden; }
  .tile-photo { position: absolute; inset: 0; }
  .photo-coat { background: linear-gradient(120deg, var(--coat-grey) 0%, #c9c8c5 40%, var(--coat-dark) 75%, var(--navy) 100%); }
  .photo-shirt-light { background: linear-gradient(160deg, #fafaf9 0%, var(--mist) 50%, var(--mist-deep) 100%); }
  .photo-shirt-soft { background: linear-gradient(200deg, #f7f6f4 0%, var(--mist) 55%, #e4e2de 100%); }
  .photo-suit { background: linear-gradient(140deg, var(--suit-light) 0%, #4a4a4c 35%, var(--suit) 70%, #151618 100%); }

  .tile-copy {
    position: absolute; inset: 0; display: flex; flex-direction: column;
    align-items: center; justify-content: center; text-align: center;
  }
  .tagline { font-size: 62px; line-height: 1.02; padding-left: 40px; }
  .collection-title { font-size: 50px; line-height: 1.05; letter-spacing: 1px; }
  .cta {
    margin-top: 20px; background: var(--button); color: var(--button-text);
    font-size: 40px; letter-spacing: 2px; padding: 4px 34px; line-height: 1.2;
  }

  .social {
    position: absolute; top: 2090px; left: 0; width: 100%;
    display: flex; justify-content: center; gap: 28px;
  }
  .social-button { width: 82px; height: 82px; background: var(--ink); border-radius: 10px; }

  .footer {
    position: absolute; top: 2248px; left: 0; width: 100%;
    text-align: center; font-size: 34px; line-height: 1.45;
  }
  .footer strong { font-weight: 700; }
</style>
</head>
<body>
<main class="email">
  <div class="brand">KOVANTA</div>

  <nav class="main-nav">
    <span class="nav-item">Watches</span>
    <span class="nav-item">Lorvane Tweed Straps</span>
  </nav>

  <h1 class="headline">WELCOME</h1>

  <section class="lookbook">
    <div class="tile">
      <div class="tile-photo photo-coat" role="img" aria-label="Man in a grey wool coat adjusting his cuff, wearing a white-dial watch on a navy tweed strap"></div>
    </div>
    <div class="tile">
      <div class="tile-photo photo-shirt-light" role="img" aria-label="Faded lifestyle photo of a man in a white shirt"></div>
      <div class="tile-copy">
        <p class="tagline">The first<br>watch with<br>Lorvane Tweed<br>Strap</p>
      </div>
    </div>
    <div class="tile">
      <div class="tile-photo photo-shirt-soft" role="img" aria-label="Faded lifestyle photo of a man in a white shirt and tie"></div>
      <div class="tile-copy">
        <p class="collection-title">VIEW OUR<br>COLLECTION</p>
        <span class="cta">HERE</span>
      </div>
    </div>
    <div class="tile">
      <div class="tile-photo photo-suit" role="img" aria-label="Man in a dark suit straightening his tie, wearing a white-dial watch on a dark strap"></div>
    </div>
  </section>

  <div class="social" aria-label="Social links">
    <span class="social-button"></span>
    <span class="social-button"></span>
    <span class="social-button"></span>
    <span class="social-button"></span>
  </div>

  <footer class="footer">
    <p>No longer want to receive these emails? You can <strong>unsubscribe here.</strong></p>
    <p>Kovanta Ltd.</p>
  </footer>
</main>
</body>
</html>
```